Casino with the 'highest winning percentage' needs a stationery design

This is for a casino in Colombo, Sri Lanka and we need a stationery design for business card, letter head and envelope.

Should be very professional, simple and elegant without fancy fonts

Reason: Not fully satisfied with the designs. Need more designs.

Industry/Entity Type

Business

Requirements
Must have
• 1. card deck symbol 'CLUBS' in red, or black

2. name in BLOCK CAPITAL LETTERS

3. Preferred font colours are black, white or red

4. Prefer 'professional /elegant' fonts
Should not have
• SHOULD NOT HAVE ANY OTHER SYMBOL EXCEPT 'CLUBS'

DO NOT PREFER ITALIC FONTS

```html
<!DOCTYPE html>
<html lang="en">
<head>
<meta charset="utf-8">
<title>Marlow's Entertainment – Stationery</title>
<link href="https://fonts.googleapis.com/css2?family=Didact+Gothic&family=Questrial&display=swap" rel="stylesheet">
<style>
  :root {
    --backdrop: #a8a8b0;
    --folder: #2b2d34;
    --folder-inner: #24262c;
    --folder-pocket: #2e3037;
    --paper: #ffffff;
    --ink: #2a2a2e;
    --ink-soft: #55565c;
    --brand-red: #a3141c;
    --silver: #c9cacf;
    --rule: #c8c8cc;
  }
  * { box-sizing: border-box; margin: 0; padding: 0; }
  html, body { width: 1200px; height: 916px; overflow: hidden; }
  body {
    background: var(--backdrop);
    position: relative;
    font-family: "Didact Gothic", "Questrial", sans-serif;
    color: var(--ink);
  }
  .piece { position: absolute; }

  /* Brand name (logo stand-in) */
  .brand { display: flex; align-items: center; gap: 8px; }
  .brand-dot { border-radius: 50%; flex: none; }
  .brand-name { text-transform: uppercase; line-height: 1.15; letter-spacing: .04em; }

  /* Folder inside */
  .folder-inside-left { left: 183px; top: 290px; width: 382px; height: 525px; background: var(--folder-inner); }
  .folder-pattern { position: absolute; right: 0; top: 0; width: 75px; height: 100%;
    background: linear-gradient(180deg, #2c2e35, #23252b); }
  .folder-inside-right { left: 565px; top: 290px; width: 375px; height: 525px; background: var(--folder-inner); }
  .insert-sheet { left: 577px; top: 297px; width: 353px; height: 335px; background: #f4f4f6; }
  .folder-pocket { left: 565px; top: 632px; width: 375px; height: 183px; background: var(--folder-pocket); }
  .card-slot { position: absolute; left: 282px; top: 14px; width: 30px; height: 30px; border-radius: 50%; background: #26282e; }
  .card-slot-low { position: absolute; left: 282px; top: 152px; width: 30px; height: 15px; border-radius: 15px 15px 0 0; background: #26282e; }
  .pocket-address { position: absolute; right: 37px; top: 75px; text-align: right; font-size: 5.2px; line-height: 7px; color: var(--silver); }
  .pocket-rule { position: absolute; left: 271px; right: 37px; top: 136px; height: 1px; background: #55575e; }
  .pocket-web { position: absolute; right: 37px; top: 140px; font-size: 6px; color: var(--silver); }

  /* Folder cover */
  .folder-cover { left: 140px; top: 235px; width: 350px; height: 510px; background: var(--folder); }
  .folder-cover .brand { position: absolute; left: 140px; top: 52px; }
  .folder-cover .brand-dot { width: 30px; height: 30px; background: var(--silver); }
  .folder-cover .brand-name { color: var(--silver); font-size: 14px; }
  .folder-cover .brand-name small { display: block; font-size: 8px; letter-spacing: .18em; margin-top: 2px; }

  /* Letterhead */
  .letterhead { left: 675px; top: 75px; width: 350px; height: 508px; background: var(--paper); }
  .letterhead .brand { position: absolute; left: 33px; top: 32px; }
  .letterhead .brand-dot { width: 22px; height: 22px; background: var(--brand-red); }
  .letterhead .brand-name { color: var(--ink); font-size: 10.5px; }
  .letterhead .brand-name small { display: block; font-size: 6px; letter-spacing: .18em; margin-top: 1px; }
  .salutation { position: absolute; left: 33px; top: 153px; font-size: 8px; font-weight: bold; font-family: "Questrial", sans-serif; }
  .letter-body { position: absolute; left: 33px; top: 168px; width: 290px; font-size: 5.4px; line-height: 7.9px; color: var(--ink-soft); text-align: justify; }
  .letter-body p + p { margin-top: 7.5px; }
  .signoff { position: absolute; right: 27px; top: 403px; text-align: right; font-size: 5.6px; color: var(--ink-soft); }
  .signoff strong { display: block; font-size: 7.5px; color: var(--ink); margin-top: 5px; font-family: "Questrial", sans-serif; }
  .signature { position: absolute; left: 180px; top: 402px; width: 92px; height: 32px; background: linear-gradient(90deg, rgba(70,90,170,.18), rgba(70,90,170,.08)); }
  .letter-footer { position: absolute; left: 33px; right: 27px; top: 488px; display: flex; font-size: 4.8px; line-height: 6.5px; color: var(--ink-soft); }
  .letter-footer > div { border-left: 1px solid var(--rule); padding-left: 4px; }
  .footer-address { width: 122px; }
  .footer-phone { width: 100px; }
  .footer-web { flex: 1; border: 0 !important; text-align: right; }
  .letter-footer b { color: var(--ink); }

  /* Business card front */
  .card-front { left: 860px; top: 75px; width: 152px; height: 83px; background: var(--paper); border: 1px solid #e2e2e6; }
  .card-front .brand { position: absolute; left: 11px; top: 15px; gap: 5px; }
  .card-front .brand-dot { width: 14px; height: 14px; background: var(--brand-red); }
  .card-front .brand-name { font-size: 6.5px; color: var(--ink); }
  .card-front .brand-name small { display: block; font-size: 3.6px; letter-spacing: .18em; }
  .card-person { position: absolute; right: 14px; top: 44px; font-size: 4.6px; font-weight: bold; color: var(--ink); text-align: left; }
  .card-person span { display: block; font-weight: normal; font-size: 3.6px; color: var(--ink-soft); }
  .card-address { position: absolute; left: 26px; top: 57px; font-size: 3.7px; line-height: 5px; color: var(--ink-soft); text-align: right; }
  .card-contacts { position: absolute; left: 98px; top: 57px; font-size: 3.7px; line-height: 5px; color: var(--ink-soft); }

  /* Business card back */
  .card-back { left: 972px; top: 657px; width: 56px; height: 153px; background: var(--folder); }
  .card-back-pattern { position: absolute; inset: 5px; background: linear-gradient(180deg, #4a4c53, #3a3c42); }
</style>
</head>
<body>

  <section class="piece folder-inside-left">
    <div class="folder-pattern" role="img" aria-label="Embossed repeating pattern on folder flap"></div>
  </section>

  <section class="piece folder-inside-right"></section>
  <div class="piece insert-sheet"></div>
  <section class="piece folder-pocket">
    <div class="card-slot"></div>
    <div class="pocket-address">MARLOW'S LIMITED<br>12, Harbour View Road<br>Colombo 01000, Sri Lanka<br>Tel: +94 11 2000450<br>Fax: +94 11 2000451</div>
    <div class="pocket-rule"></div>
    <div class="pocket-web">www.marlowscolombo.com</div>
    <div class="card-slot-low"></div>
  </section>

  <section class="piece folder-cover">
    <div class="brand">
      <span class="brand-dot"></span>
      <span class="brand-name">Marlow's Entertainment<small>Sri Lanka</small></span>
    </div>
  </section>

  <article class="piece letterhead">
    <div class="brand">
      <span class="brand-dot"></span>
      <span class="brand-name">Marlow's<br>Entertainment<small>Sri Lanka</small></span>
    </div>
    <p class="salutation">Dear sir / madame,</p>
    <div class="letter-body">
      <p>Lorem ipsum dolor sit amet, consectetur adipisicing elit, sed do eiusmod tempor incididunt ut labore et dolore magna aliqua. Ut enim ad minim veniam, quis nostrud exercitation ullamco laboris nisi ut aliquip ex ea commodo consequat. Duis aute irure dolor in reprehenderit in voluptate velit esse cillum dolore eu fugiat nulla pariatur. Excepteur sint occaecat cupidatat non proident, sunt in culpa qui officia deserunt mollit anim id est laborum. Lorem ipsum dolor sit amet, consectetur adipisicing elit, sed do eiusmod tempor incididunt ut labore et dolore magna aliqua. Ut enim ad minim veniam, quis nostrud exercitation ullamco laboris nisi ut aliquip ex ea commodo consequat. Duis aute irure dolor in reprehenderit in voluptate velit esse cillum dolore eu fugiat nulla pariatur. Excepteur sint occaecat cupidatat non proident, sunt in culpa qui officia deserunt mollit anim id est laborum.</p>
      <p>Lorem ipsum dolor sit amet, consectetur adipisicing elit, sed do eiusmod tempor incididunt ut labore et dolore magna aliqua. Ut enim ad minim veniam, quis nostrud exercitation ullamco laboris nisi ut aliquip ex ea commodo consequat. Duis aute irure dolor in reprehenderit in voluptate velit esse cillum dolore eu fugiat nulla pariatur. Excepteur sint occaecat cupidatat non proident, sunt in culpa qui officia deserunt mollit anim id est laborum.</p>
      <p>Lorem ipsum dolor sit amet, consectetur adipisicing elit, sed do eiusmod tempor incididunt ut labore et dolore magna aliqua. Ut enim ad minim veniam, quis nostrud exercitation ullamco laboris nisi ut aliquip ex ea commodo consequat. Duis aute irure dolor in reprehenderit in voluptate velit esse cillum dolore eu fugiat nulla pariatur. Excepteur sint occaecat cupidatat non proident, sunt in culpa qui officia deserunt mollit anim id est laborum.</p>
      <p>Lorem ipsum dolor sit amet, consectetur adipisicing elit, sed do eiusmod tempor incididunt ut labore et dolore magna aliqua. Ut enim ad minim veniam, quis nostrud exercitation ullamco laboris nisi ut aliquip ex ea commodo consequat. Duis aute irure dolor in reprehenderit in voluptate velit esse cillum dolore eu fugiat nulla pariatur. Excepteur sint occaecat cupidatat non proident, sunt in culpa qui officia deserunt mollit anim id est laborum.</p>
    </div>
    <div class="signature" role="img" aria-label="Handwritten signature in blue ink"></div>
    <div class="signoff">Yours Sincerely,<strong>Nila Perera</strong></div>
    <footer class="letter-footer">
      <div class="footer-address">12, Harbour View Road<br>Colombo 01000, Sri Lanka</div>
      <div class="footer-phone"><b>Tel:</b> +94 11 2000450<br><b>Fax:</b> +94 11 2000451</div>
      <div class="footer-web">www.marlowscolombo.com</div>
    </footer>
  </article>

  <aside class="piece card-front">
    <div class="brand">
      <span class="brand-dot"></span>
      <span class="brand-name">Marlow's<br>Entertainment<small>Sri Lanka</small></span>
    </div>
    <div class="card-person">DEV FERNANDO<span>Casino Manager</span></div>
    <div class="card-address">MARLOW'S LIMITED<br>12, Harbour View Road<br>Colombo 01000, Sri Lanka</div>
    <div class="card-contacts">Tel: +94 11 2000450<br>Fax: +94 11 2000451<br>www.marlowscolombo.com</div>
  </aside>

  <aside class="piece card-back">
    <div class="card-back-pattern" role="img" aria-label="Repeating silver pattern on business card back"></div>
  </aside>

</body>
</html>
```